Business Card Design Project

Lumen Clinic Group

Dr Tomas Feldren M.D, F.R.C.S
Vascular and Vein Surgery

18-46 Corbell Avenue, Suite 317
Astoria
NY 11290

212-555-0163
718-555-0147
www.palemedic.example back of the card for scheduled appointments up to 5 appointment dates

Target Market(s)

Male and Female patients from 25 onwards with spider veins or varicose veins

Industry/Entity Type

Business

Font styles to use
Serif

Colors
86cae6
85abd2
0456a4

Requirements
Must have
• Modern Sophisticated design using light blue and grey text
Should not have
• hearts or flowers

```html
<!DOCTYPE html>
<html lang="en">
<head>
<meta charset="utf-8">
<title>Lumen Clinic Group – Business Card</title>
<link rel="stylesheet" href="https://fonts.googleapis.com/css2?family=Open+Sans:wght@400;600;700&display=swap">
<style>
  :root {
    --sky: #86cae6;
    --cyan: #1fa9d9;
    --periwinkle: #85abd2;
    --navy: #0456a4;
    --grey-text: #555b60;
    --dark-text: #2a2d30;
    --charcoal: #3b3e42;
    --paper: #ffffff;
    --stage: #e9ecef;
  }
  * { box-sizing: border-box; margin: 0; padding: 0; }
  html, body { width: 1200px; height: 800px; overflow: hidden; }
  body {
    background: var(--stage);
    font-family: "Open Sans", sans-serif;
    display: flex;
    align-items: center;
    justify-content: center;
    gap: 40px;
  }
  .card {
    position: relative;
    width: 520px;
    height: 297px;
    border-radius: 3px;
    overflow: hidden;
    box-shadow: 0 6px 18px rgba(0,0,0,0.18);
  }

  /* Front */
  .card-front { background: var(--paper); }
  .doctor { position: absolute; left: 30px; top: 30px; }
  .doctor-name { color: var(--cyan); font-weight: 600; font-size: 17px; white-space: nowrap; }
  .doctor-title { color: var(--grey-text); font-size: 12px; margin-top: 2px; }
  .brand {
    position: absolute; right: 30px; top: 84px;
    color: var(--navy); font-weight: 700; font-size: 27px; letter-spacing: 0.3px;
    white-space: nowrap;
  }
  .contact {
    position: absolute; left: 230px; top: 150px;
    color: var(--dark-text); font-size: 13.5px; line-height: 1.45;
    white-space: nowrap;
  }
  .contact-line { display: flex; align-items: center; gap: 7px; }
  .contact-line svg { width: 13px; height: 13px; flex: none; }
  .band { position: absolute; left: 0; right: 0; bottom: 0; height: 38px; }
  .band-web {
    position: absolute; left: 0; bottom: 0; width: 200px; height: 38px;
    background: var(--cyan); color: var(--paper);
    font-size: 12px; display: flex; align-items: center; padding-left: 28px;
    clip-path: polygon(0 0, 88% 0, 100% 100%, 0 100%);
    white-space: nowrap;
  }
  .band-grey {
    position: absolute; left: 0; right: 0; bottom: 0; height: 24px;
    background: var(--charcoal);
  }

  /* Back */
  .card-back {
    background: linear-gradient(135deg, var(--navy) 0%, #0b74c2 55%, var(--cyan) 100%);
  }
  .schedule {
    position: absolute; left: 18px; right: 18px; top: 16px; height: 200px;
    background: var(--paper); border-radius: 6px; padding: 12px 18px;
  }
  .schedule-title { color: var(--grey-text); font-size: 13px; margin-bottom: 6px; }
  .slot {
    display: grid; grid-template-columns: 40px 1fr 40px 1fr;
    gap: 6px; align-items: end; height: 30px;
    color: var(--grey-text); font-size: 12px;
  }
  .slot .rule { border-bottom: 1px solid var(--dark-text); height: 14px; margin-right: 14px; }
  .back-brand {
    position: absolute; right: 24px; bottom: 26px;
    color: var(--paper); font-weight: 600; font-size: 22px; letter-spacing: 0.5px;
    white-space: nowrap;
  }
</style>
</head>
<body>
  <section class="card card-front" aria-label="Business card front">
    <div class="doctor">
      <p class="doctor-name">Dr Tomas Feldren M.D, F.R.C.S</p>
      <p class="doctor-title">Vascular and Vein Surgery</p>
    </div>
    <p class="brand">Lumen Clinic Group</p>
    <div class="contact">
      <p>18-46 Corbell Avenue, Suite 317</p>
      <p>Astoria, NY 11290</p>
      <p class="contact-line">
        <svg viewBox="0 0 16 16" aria-hidden="true"><circle cx="8" cy="8" r="8" fill="#1fa9d9"/><path d="M5.2 4.2l1.6-.4.9 2-1 .8a5 5 0 0 0 2.7 2.7l.8-1 2 .9-.4 1.6c-3.6.3-6.9-3-6.6-6.6z" fill="#fff"/></svg>
        212-555-0163
      </p>
      <p class="contact-line">
        <svg viewBox="0 0 16 16" aria-hidden="true"><circle cx="8" cy="8" r="8" fill="#1fa9d9"/><rect x="5.5" y="3.5" width="5" height="9" rx="1" fill="#fff"/><rect x="6.5" y="5" width="3" height="5" fill="#1fa9d9"/></svg>
        718-555-0147
      </p>
    </div>
    <div class="band">
      <div class="band-grey"></div>
      <div class="band-web">www.palemedic.example</div>
    </div>
  </section>

  <section class="card card-back" aria-label="Business card back">
    <div class="schedule">
      <p class="schedule-title">Appointments</p>
      <div class="slot"><span>Date:</span><span class="rule"></span><span>Time:</span><span class="rule"></span></div>
      <div class="slot"><span>Date:</span><span class="rule"></span><span>Time:</span><span class="rule"></span></div>
      <div class="slot"><span>Date:</span><span class="rule"></span><span>Time:</span><span class="rule"></span></div>
      <div class="slot"><span>Date:</span><span class="rule"></span><span>Time:</span><span class="rule"></span></div>
      <div class="slot"><span>Date:</span><span class="rule"></span><span>Time:</span><span class="rule"></span></div>
    </div>
    <p class="back-brand">Lumen Clinic Group</p>
  </section>
</body>
</html>
```